Craft a new attractive & professional PowerPoint presentation based on the material provided

Dear Designer,
We are looking for a fresh revamp of our Corporate Power Point presentation. Please find attached:
- the current ppt file;
- new pdf with Corporate profile;
- our logo.
For more information please consult our Social Media Channels:
LinkedIn: https://www.linkedin.com/company/7416092/admin/
IG: https://www.instagram.com/korvalbristle/
YT: https://www.youtube.com/channel/UCmQaRtZoPeWnKxLbVdTyrfa
Deadline: before November 20th 2022.
Please do not hesitate to reach out for any questions.
Best wishes,
KVL Marketing Team
Font styles to use
Other font styles liked:
- Helvetica types
Colors
Designer to choose colors to be used in the design.
Look and feel
Each slider illustrates characteristics of the customer's brand and the style your logo design should communicate.

```html
<!DOCTYPE html>
<html lang="en">
<head>
<meta charset="utf-8">
<title>KVL Corporate Presentation</title>
<link rel="stylesheet" href="https://fonts.googleapis.com/css2?family=Archivo:wght@400;600;700;800&display=swap">
<style>
:root{
  --red:#e31e24;
  --red-dark:#b5141a;
  --grey-bg:#d4d4d4;
  --panel:#e6e6e6;
  --ink:#333;
  --white:#fff;
}
*{box-sizing:border-box;margin:0;padding:0}
html,body{width:1200px;height:2441px;overflow:hidden}
body{background:var(--grey-bg);font-family:"Archivo",Helvetica,Arial,sans-serif;color:var(--ink);position:relative}
.stage{position:absolute;left:0;top:0;width:1200px;height:730px;background:linear-gradient(180deg,#e9ecef,#cfd2d6)}
.slide{position:absolute;width:563px;height:316px;background:var(--white);overflow:hidden}
.hero{left:161px;top:118px;transform:scale(1.56);transform-origin:0 0;box-shadow:0 10px 30px rgba(0,0,0,.2)}
.photo{position:absolute}
.cover-photo{left:0;top:0;width:563px;height:247px;background:linear-gradient(120deg,#e4262c 0%,#c8262c 45%,#e84a4f 75%,#d92a30 100%)}
.cover-photo.dark{background:linear-gradient(120deg,#2a2a2a 0%,#3a2626 45%,#5a2a2c 75%,#2c2c2c 100%)}
.faint{position:absolute;color:rgba(255,255,255,.14);font-weight:800;transform:rotate(-22deg);font-size:26px;letter-spacing:1px}
.cover-title{position:absolute;top:55px;font-size:28px;line-height:32px;color:var(--white);font-weight:400}
.cover-title b{font-weight:700}
.cover-title.red{color:var(--red);font-weight:700}
.cover-sub{position:absolute;top:121px;width:200px;font-size:7.2px;line-height:8.4px;color:var(--white);text-transform:uppercase}
.date{position:absolute;top:175px;width:111px;height:16px;border:1px solid var(--white);border-radius:2px;color:var(--white);font-size:6.5px;font-weight:600;display:flex;align-items:center;justify-content:center}
.date.filled{background:var(--red);border-color:var(--red)}
.footnote{position:absolute;top:279px;font-size:5.6px;color:#777}
.logo{position:absolute;background:var(--red);border:4px solid var(--white);border-radius:8px;color:var(--white);font-weight:800;display:flex;align-items:center;justify-content:center;letter-spacing:1px}
.logo.big{width:80px;height:80px;font-size:27px;top:207px}
.logo.mini{width:32px;height:32px;left:25px;top:270px;border:0;border-radius:4px;font-size:11px}
.pagenum{position:absolute;right:14px;top:289px;width:12px;height:12px;border-radius:50%;background:var(--red);color:var(--white);font-size:6px;display:flex;align-items:center;justify-content:center}
.heading{position:absolute;left:0;width:100%;text-align:center;top:22px;font-size:20px;font-weight:700;color:var(--red)}
.caption{position:absolute;font-size:9.5px;text-align:center;line-height:11px}
.fact{position:absolute;top:106px;width:124px;height:124px;background:var(--panel);border-radius:4px;text-align:center;font-size:9.5px;line-height:11px;padding-top:19px}
.fact.red{background:var(--red);color:var(--white)}
.fact .num{position:absolute;left:0;right:0;top:72px;font-size:23px;font-weight:700;line-height:24px}
.fact .unit{position:absolute;left:0;right:0;top:101px;font-size:8.5px}
.solution-box{position:absolute;top:110px;width:124px;height:124px;background:var(--red);border-radius:4px;color:var(--white);text-align:center;font-size:9.5px;line-height:11px;display:flex;flex-direction:column;align-items:center;justify-content:center;padding:0 10px}
.solution-box .num{font-size:21px;font-weight:700;line-height:26px}
.section-title{position:absolute;font-size:21px;font-weight:700;color:var(--red);line-height:23px}
.body-text{position:absolute;font-size:9.5px;line-height:11px}
.body-text p{margin-bottom:7px}
</style>
</head>
<body>

<div class="stage"></div>

<!-- Hero cover -->
<section class="slide hero">
  <div class="photo cover-photo" role="img" aria-label="Worker in a red shirt holding an industrial brush"></div>
  <span class="faint" style="left:170px;top:180px">korvalbristle.com</span>
  <h1 class="cover-title" style="left:56px">YOUR <b>BRUSH</b><br><b>SOLUTION</b></h1>
  <p class="cover-sub" style="left:56px">Driving excellence and keeping on developing innovative products thanks to our incredible team of talents.</p>
  <div class="date" style="left:56px">November 8, 2022</div>
  <p class="footnote" style="left:56px">© Industrial Brushes KVL Korval Spazzole Industriali, Bologna - Italy</p>
  <div class="logo big" style="left:455px">KVL</div>
</section>

<!-- Row 1 -->
<section class="slide" style="left:28px;top:750px">
  <div class="photo cover-photo" role="img" aria-label="Worker in a red shirt holding an industrial brush"></div>
  <span class="faint" style="left:170px;top:180px">korvalbristle.com</span>
  <h2 class="cover-title" style="left:56px">YOUR <b>BRUSH</b><br><b>SOLUTION</b></h2>
  <p class="cover-sub" style="left:56px">Driving excellence and keeping on developing innovative products thanks to our incredible team of talents.</p>
  <div class="date" style="left:56px">November 8, 2022</div>
  <p class="footnote" style="left:56px">© Industrial Brushes KVL Korval Spazzole Industriali, Bologna - Italy</p>
  <div class="logo big" style="left:455px">KVL</div>
</section>

<section class="slide" style="left:609px;top:750px">
  <div class="photo cover-photo" role="img" aria-label="Worker in a red shirt seen from the back"></div>
  <span class="faint" style="left:160px;top:180px">korvalbristle.com</span>
  <h2 class="cover-title" style="left:279px">YOUR <b>BRUSH</b><br><b>SOLUTION</b></h2>
  <p class="cover-sub" style="left:279px">Driving excellence and keeping on developing innovative products thanks to our incredible team of talents.</p>
  <div class="date" style="left:279px">November 8, 2022</div>
  <p class="footnote" style="left:279px">© Industrial Brushes KVL Korval Spazzole Industriali, Bologna - Italy</p>
  <div class="logo big" style="left:30px">KVL</div>
</section>

<!-- Row 2 -->
<section class="slide" style="left:28px;top:1085px">
  <div class="photo cover-photo dark" role="img" aria-label="Worker in a red shirt holding an industrial brush, dark tone"></div>
  <span class="faint" style="left:170px;top:180px">korvalbristle.com</span>
  <h2 class="cover-title red" style="left:56px">YOUR BRUSH<br>SOLUTION</h2>
  <p class="cover-sub" style="left:56px">Driving excellence and keeping on developing innovative products thanks to our incredible team of talents.</p>
  <div class="date filled" style="left:56px">November 8, 2022</div>
  <p class="footnote" style="left:56px">© Industrial Brushes KVL Korval Spazzole Industriali, Bologna - Italy</p>
  <div class="logo big" style="left:455px">KVL</div>
</section>

<section class="slide" style="left:609px;top:1085px">
  <h2 class="heading">A FAMILY COMPANY</h2>
  <div class="photo" style="left:25px;top:72px;width:512px;height:156px;background:linear-gradient(180deg,#b9c4cc 0%,#c9b49a 45%,#5b6a6a 70%,#3d4040 100%)" role="img" aria-label="Company team posing in front of the factory"></div>
  <p class="caption" style="left:0;width:100%;top:240px">Driving excellence and keeping on developing<br>innovative products thanks to our incredible Team of Talents.</p>
  <div class="logo mini">KVL</div>
  <div class="pagenum">4</div>
</section>

<!-- Row 3 -->
<section class="slide" style="left:28px;top:1419px">
  <h2 class="heading">KEY FACTS</h2>
  <div class="fact red" style="left:17px">One of the oldest<br>family owned<br>businesses in Italy:<span class="num">110+</span><span class="unit">years</span></div>
  <div class="fact" style="left:152px">Leading player<br>on the brush market<br><br>Turnover 2021, €:<span class="num">15,6</span><span class="unit">mln</span></div>
  <div class="fact" style="left:286px">We drive excellence<br>thanks to our team of<br>talents in Italy,<br>Romania &amp; Spain:<span class="num">115+</span><span class="unit">talents</span></div>
  <div class="fact" style="left:421px">We offer a wide<br>range of solutions<br>b2b &amp; b2c:<span class="num">2000+</span><span class="unit">SKUs</span></div>
  <div class="logo mini">KVL</div>
  <div class="pagenum">5</div>
</section>

<section class="slide" style="left:609px;top:1419px">
  <div class="photo" style="left:27px;top:74px;width:507px;height:168px;background:radial-gradient(circle at 75% 60%,#f0585c,#d8262c 60%,#c01c22)" role="img" aria-label="Close-up of red industrial brushes"></div>
  <h2 class="cover-title" style="left:67px;top:100px;font-size:27px;line-height:30px">OUR <b>SOLUTIONS</b><br>TO <b>MEET</b><br>YOUR <b>NEEDS</b></h2>
  <div class="logo big" style="left:430px;top:206px;width:72px;height:72px;font-size:24px">KVL</div>
</section>

<!-- Row 4 -->
<section class="slide" style="left:28px;top:1755px">
  <h2 class="heading">OUR PROFESSIONAL SOLUTIONS</h2>
  <div class="photo" style="left:-60px;top:60px;width:132px;height:200px;border-radius:50%;background:radial-gradient(circle,#f2f2f2 15%,#9a9a9a 40%,#cfcfcf 60%,#7a7a7a 90%)" role="img" aria-label="Steel wire wheel brush"></div>
  <div class="photo" style="left:500px;top:70px;width:110px;height:190px;border-radius:45%;background:linear-gradient(180deg,#e02a30 0%,#b51a20 45%,#8a8a8a 60%,#4a4a4a 100%)" role="img" aria-label="Cup brush with red housing"></div>
  <div class="solution-box" style="left:87px">Broad product offer requires constant attention to high quality standards and maximum production flexibility</div>
  <div class="solution-box" style="left:219px"><span class="num">2,000+</span>SKUs are available in our catalogue</div>
  <div class="solution-box" style="left:351px"><span class="num">600+</span>are on stock, ready for pick up &amp; delivery</div>
  <div class="logo mini">KVL</div>
  <div class="pagenum">7</div>
</section>

<section class="slide" style="left:609px;top:1755px">
  <div style="position:absolute;left:0;top:0;width:100%;height:183px;background:var(--red)"></div>
  <h2 class="heading" style="color:var(--white)">OUR SPORTS DIVISION</h2>
  <p class="caption" style="left:0;width:100%;top:75px;color:var(--white)">Our high <b>Quality &amp; Secure</b> solutions are designed for athletes who practice ski-jump,<br>downhill or cross-country skiing <b>all year round</b>.</p>
  <div class="photo" style="left:25px;top:122px;width:251px;height:120px;border:2px solid var(--white);background:linear-gradient(180deg,#7d8a5a,#5f9a5a 50%,#8a8a6a)" role="img" aria-label="Ski-jump hill covered with green synthetic bristles"></div>
  <div class="photo" style="left:286px;top:122px;width:252px;height:120px;border:2px solid var(--white);background:linear-gradient(160deg,#1e4fc9,#2a5fd8 55%,#16399a)" role="img" aria-label="Skiers on blue synthetic downhill slope"></div>
  <p class="caption" style="left:25px;width:251px;top:249px;font-size:7px">SALTO CON GLI SCI / SKI-JUMP</p>
  <p class="caption" style="left:286px;width:252px;top:249px;font-size:7px">SCI DA DISCESA / DOWNHILL SKI</p>
  <div class="logo mini">KVL</div>
  <div class="pagenum">8</div>
</section>

<!-- Row 5 -->
<section class="slide" style="left:28px;top:2089px">
  <h2 class="section-title" style="left:56px;top:48px">CONTINIOUS<br>COMITTMENT<br>TO EXCELLENCE</h2>
  <div style="position:absolute;left:275px;top:56px;width:48px;height:48px;border-radius:50%;background:#1f5fa8" role="img" aria-label="Certification body badge"></div>
  <div class="body-text" style="left:56px;top:132px;width:265px">
    <p><b>KVL</b> is certified by NordCert following quality standard of <b>ISO 9001:2015</b>.</p>
    <p>Our brushes are carefully tested in accordance with the <b>UNI EN 1083</b> safety regulations concerning their manufacture and use.</p>
    <p>All our products are performance assessed by our internal quality department.</p>
  </div>
  <div class="photo" style="left:352px;top:24px;width:170px;height:245px;background:linear-gradient(90deg,#1f3f8f 0 10px,#f4f4f4 10px);box-shadow:0 1px 4px rgba(0,0,0,.25)" role="img" aria-label="ISO 9001 quality certificate document"></div>
  <div class="logo mini">KVL</div>
  <div class="pagenum">9</div>
</section>

<section class="slide" style="left:609px;top:2089px">
  <h2 class="section-title" style="left:56px;top:50px">ONGOING<br>INNOVATION</h2>
  <div class="body-text" style="left:56px;top:122px;width:225px">
    <p>Innovation is at the heart of our values and development strategy.</p>
    <p>With so many years of technical expertise, we develop dedicated solutions to meet your specific needs.</p>
    <p>Our recognized know-how goes hand in hand with ongoing innovation, quality and customer satisfaction.</p>
  </div>
  <div class="photo" style="left:305px;top:0;width:216px;height:270px;background:linear-gradient(180deg,#cfe2ea 0%,#8fa8b6 40%,#3b4a6a 70%,#2a3350 100%)" role="img" aria-label="Audience attending a technology conference presentation"></div>
  <div class="logo mini">KVL</div>
  <div class="pagenum">10</div>
</section>

</body>
</html>
```